Brambury Logistics

Create a modern, simple, Elegant business card design for my business.

Services: Tamo Trucks, Transport, Contract Logistics,

Industry/Entity Type

Business

Contact Information for Business Card

Include all details same as old card plus new website address: www.bramburylogistics.com.au

Requirements
Must have
• Similar colors to Logo.

```html
<!DOCTYPE html>
<html lang="en">
<head>
<meta charset="utf-8">
<title>Brambury Logistics – Business Card</title>
<link href="https://fonts.googleapis.com/css2?family=Exo+2:wght@700&family=Roboto:wght@400;500&display=swap" rel="stylesheet">
<style>
  :root{
    --bg:#e4e4e4;
    --blue-deep:#0d5a8a;
    --blue-mid:#1a7fb5;
    --blue-bright:#1b8fd0;
    --white:#ffffff;
    --card-light:#f7f7f7;
    --ink:#333639;
    --logo-grey:#4a4d52;
    --swoosh-dark:#2e3033;
    --swoosh-grey:#8c8f93;
  }
  *{box-sizing:border-box;margin:0;padding:0}
  html,body{width:1200px;height:576px;overflow:hidden;background:var(--bg)}
  .canvas{position:relative;width:1200px;height:576px}
  .card{position:absolute;top:138px;height:292px;border-radius:11px;overflow:hidden;
        box-shadow:0 3px 8px rgba(0,0,0,.22)}

  /* Front */
  .card--front{left:82px;width:484px;
        background:linear-gradient(180deg,var(--blue-deep) 0%,var(--blue-mid) 100%)}
  .front__scene{position:absolute;left:130px;top:50px;width:240px;height:190px;
        background:radial-gradient(ellipse at center,rgba(255,255,255,.08),rgba(255,255,255,0) 70%)}
  .front__brand{position:absolute;left:0;right:0;top:118px;text-align:center;
        font-family:'Roboto',sans-serif;font-weight:500;font-size:31px;color:var(--white);letter-spacing:.5px}
  .front__services{position:absolute;left:0;right:0;bottom:29px;display:flex;justify-content:center;gap:15px;
        font-family:'Roboto',sans-serif;font-size:11.5px;color:var(--white);letter-spacing:.3px}

  /* Back */
  .card--back{left:602px;width:480px;background:var(--card-light)}
  .back__wave{position:absolute;left:0;top:0}
  .back__person{position:absolute;right:28px;top:30px;text-align:right;color:var(--white)}
  .back__name{font-family:'Exo 2',sans-serif;font-weight:700;font-size:19px;letter-spacing:.5px}
  .back__role{font-family:'Roboto',sans-serif;font-size:11px;margin-top:1px}
  .back__brand{position:absolute;left:34px;top:112px;
        font-family:'Roboto',sans-serif;font-weight:500;font-size:27px;color:var(--logo-grey)}
  .contact{position:absolute;left:30px;top:213px;list-style:none;
        font-family:'Roboto',sans-serif;font-size:12.5px;color:var(--ink)}
  .contact li{display:flex;align-items:center;height:17px}
  .contact svg{width:11px;height:11px;margin-right:12px;fill:var(--blue-bright)}
  .services{position:absolute;right:28px;top:216px;text-align:right;list-style:none;
        font-family:'Roboto',sans-serif;font-size:12.5px;color:var(--ink)}
  .services li{height:16px}
  .services .mark{color:var(--blue-bright);margin-left:5px}
</style>
</head>
<body>
<div class="canvas">

  <section class="card card--front">
    <div class="front__scene" role="img" aria-label="Faint photo of a truck on a road"></div>
    <div class="front__brand">Brambury Logistics</div>
    <div class="front__services">
      <span>TAMO TRUCKS</span><span>TRANSPORT</span><span>CONTRACT LOGISTICS</span><span>HOTSHOTS</span>
    </div>
  </section>

  <section class="card card--back">
    <svg class="back__wave" width="480" height="160" viewBox="0 0 480 160" aria-hidden="true">
      <defs>
        <linearGradient id="waveBlue" x1="0" y1="0" x2="0" y2="1">
          <stop offset="0" stop-color="#1b8fd0"/>
          <stop offset="1" stop-color="#0c5f96"/>
        </linearGradient>
      </defs>
      <path d="M0,0 H480 V130 C400,128 330,98 250,58 C170,18 80,16 0,34 Z" fill="url(#waveBlue)"/>
      <path d="M0,36 C80,12 170,14 280,66 C180,30 90,30 0,52 Z" fill="var(--swoosh-dark)"/>
      <path d="M90,30 C200,22 262,62 330,110 C380,140 430,144 480,144" fill="none" stroke="var(--swoosh-grey)" stroke-width="4"/>
    </svg>

    <div class="back__person">
      <div class="back__name">Daniel Reeve</div>
      <div class="back__role">Managing Director</div>
    </div>

    <div class="back__brand">Brambury Logistics</div>

    <ul class="contact">
      <li><svg viewBox="0 0 12 12"><path d="M1 4c0-2 2-3 5-3s5 1 5 3l-2 1-1-2H4L3 5zM3 6h6l1 5H2z"/></svg>0400 382 615</li>
      <li><svg viewBox="0 0 12 12"><path d="M6 0a6 6 0 1 0 0 12A6 6 0 0 0 6 0zm0 1c1 1 1.6 2.5 1.7 4.5H4.3C4.4 3.5 5 2 6 1zM1 6.5h2.3c.1 1.8.6 3.2 1.3 4.2A5 5 0 0 1 1 6.5zm0-1a5 5 0 0 1 3.6-4.2C3.9 2.3 3.4 3.7 3.3 5.5zm5 5.5c-1-1-1.6-2.5-1.7-4.5h3.4C7.6 8.5 7 10 6 11zm1.4-.3c.7-1 1.2-2.4 1.3-4.2H11a5 5 0 0 1-3.6 4.2zM8.7 5.5c-.1-1.8-.6-3.2-1.3-4.2A5 5 0 0 1 11 5.5z"/></svg>www.bramburylogistics.com.au</li>
      <li><svg viewBox="0 0 12 12"><path d="M0 2h12v8H0zm1 1v.3l5 3.5 5-3.5V3zm0 1.6V9h10V4.6L6 8z"/></svg>dan@bramburylogistics.com.au</li>
    </ul>

    <ul class="services">
      <li>Tamo Trucks<span class="mark">«</span></li>
      <li>Contract Logistics<span class="mark">«</span></li>
      <li>Hotshots<span class="mark">«</span>&nbsp; Transport<span class="mark">«</span></li>
    </ul>
  </section>

</div>
</body>
</html>
```